Harlowe plumbing business cards

Want a functional designed for my business cards using my logo

Company Name- Harlowe Plumbing, Heating & Water Systems
Name- Marcus Harlowe
Title- Vice President
Cell- 555-318-7426
Email- Harloweplumbing@mailbrook.net
Business address-
PO Box 37
Fenwick Mill, MD 21999

Industry/Entity Type

Plumbing

```html
<!DOCTYPE html>
<html lang="en">
<head>
<meta charset="utf-8">
<title>Harlowe Plumbing – Business Cards</title>
<link rel="stylesheet" href="https://fonts.googleapis.com/css2?family=Roboto+Condensed:wght@300;700&family=Source+Sans+3:wght@400;500&display=swap">
<style>
  :root {
    --stage: #9b9b9b;
    --card-black: #111111;
    --brand-blue: #0a6fbf;
    --pipe-blue: #9ab4e2;
    --text-white: #ffffff;
    --divider: #555555;
  }
  * { margin: 0; padding: 0; box-sizing: border-box; }
  html, body { width: 1133px; height: 1200px; overflow: hidden; background: var(--stage); }
  body { position: relative; font-family: "Source Sans 3", sans-serif; color: var(--text-white); }

  .card { position: absolute; left: 215px; width: 704px; height: 410px; background: var(--card-black); overflow: hidden; }
  .card--back { top: 146px; }
  .card--front { top: 643px; }

  /* back */
  .back-wordmark {
    position: absolute; left: 0; right: 0; top: 150px; text-align: center;
    font-size: 50px; font-weight: 500; color: var(--brand-blue); letter-spacing: 0.5px;
  }
  .back-url {
    position: absolute; left: 0; right: 0; top: 350px; text-align: center;
    font-size: 21px; letter-spacing: 3px; color: var(--text-white);
  }
  .back-url .domain { color: var(--brand-blue); font-weight: 500; }

  /* front */
  .front-bands { position: absolute; inset: 0; }
  .person { position: absolute; right: 26px; top: 28px; text-align: right; font-family: "Roboto Condensed", sans-serif; }
  .person__name { font-size: 25px; font-weight: 700; line-height: 1.1; }
  .person__title { font-size: 22px; font-weight: 300; line-height: 1.3; }

  .company-name {
    position: absolute; left: 34px; top: 160px; width: 300px;
    font-size: 34px; font-weight: 500; line-height: 1.05; color: var(--text-white);
  }

  .contact-list { position: absolute; left: 36px; top: 306px; list-style: none; }
  .contact-list li { display: flex; align-items: center; height: 32px; font-size: 18px; }
  .contact-list svg { width: 18px; height: 18px; margin-right: 10px; fill: none; stroke: var(--pipe-blue); stroke-width: 1.6; }

  .divider { position: absolute; left: 341px; top: 345px; width: 1px; height: 50px; background: var(--divider); }
  .address { position: absolute; left: 362px; top: 342px; font-size: 18px; line-height: 29px; }
</style>
</head>
<body>

<section class="card card--back" aria-label="Business card back">
  <div class="back-wordmark">Harlowe Plumbing</div>
  <div class="back-url">www.<span class="domain">harloweplumbing</span>.com</div>
</section>

<section class="card card--front" aria-label="Business card front">
  <svg class="front-bands" viewBox="0 0 704 410" width="704" height="410" aria-hidden="true">
    <polygon points="0,0 704,0 704,262 202,12 0,106" fill="var(--brand-blue)"/>
    <polyline points="0,114 202,20 704,274" fill="none" stroke="var(--pipe-blue)" stroke-width="5"/>
  </svg>

  <div class="person">
    <div class="person__name">Marcus Harlowe</div>
    <div class="person__title">Vice President</div>
  </div>

  <div class="company-name">Harlowe Plumbing, Heating &amp; Water Systems</div>

  <ul class="contact-list">
    <li>
      <svg viewBox="0 0 18 18"><path d="M4 2l3 3-2 2c1 2.5 3 4.5 5.5 5.5l2-2 3 3-2 2.5C8 15 3 10 1.5 4z"/></svg>
      555-204-6139
    </li>
    <li>
      <svg viewBox="0 0 18 18"><circle cx="9" cy="9" r="8"/><rect x="6.5" y="4.5" width="5" height="9" rx="1"/></svg>
      555-318-7426
    </li>
    <li>
      <svg viewBox="0 0 18 18"><rect x="1" y="4" width="16" height="11"/><path d="M1 4l8 6 8-6M1 15l6-5M17 15l-6-5"/></svg>
      Harloweplumbing@mailbrook.net
    </li>
  </ul>

  <div class="divider"></div>
  <div class="address">PO Box 37<br>Fenwick Mill, MD 21999</div>
</section>

</body>
</html>
```